Youth Lifting Youth Business Card. We have existing logo

We need a business card design from an existing logo.
Our logo is in black and white but would love to add in the color burgundy but we're open to any color. Our website is www.brightmeadowfund.org

Target Market(s)

corporations and foundations who will be donating

Industry/Entity Type

Business

Contact Information for Business Card

Address: 2316 Whitcombe Ave Harlow Springs, NV 93147
Name: Morgan Falkner
Founder email: morgan.falkner@brightmeadowfund.org
Phone: 541-317-6089

Requirements
Nice to have
• Our colors are burgundy and white, but that's not a necessity

```html
<!DOCTYPE html>
<html lang="en">
<head>
<meta charset="utf-8">
<title>Bright Meadow Fund – Business Card</title>
<link rel="stylesheet" href="https://fonts.googleapis.com/css2?family=Arimo:wght@400&display=swap">
<style>
  :root {
    --page-bg: #e6e3de;
    --card-bg: #f7f7f7;
    --ink: #1a1a1a;
    --band: #141414;
    --muted: #3a3a3a;
    --mark-fill: #ffffff;
  }
  * { box-sizing: border-box; margin: 0; padding: 0; }
  html, body { width: 1200px; height: 901px; overflow: hidden; }
  body {
    background: var(--page-bg);
    font-family: "Arimo", Arial, sans-serif;
    color: var(--ink);
    display: flex;
    align-items: center;
    justify-content: center;
    gap: 44px;
  }
  .card {
    position: relative;
    width: 540px;
    height: 309px;
    background: var(--card-bg);
    box-shadow: 0 6px 18px rgba(0,0,0,0.18);
    overflow: hidden;
  }
  .card__band {
    position: absolute;
    left: 0; top: 0;
    width: 120px; height: 309px;
  }
  .brand {
    position: absolute;
    left: 40px; top: 22px;
    display: flex;
    align-items: center;
    gap: 12px;
  }
  .brand__dot {
    width: 96px; height: 96px;
    border-radius: 50%;
    background: var(--mark-fill);
  }
  .brand__name {
    font-size: 15px;
    line-height: 1.2;
    color: var(--ink);
    white-space: nowrap;
  }
  .contact {
    position: absolute;
    left: 150px; bottom: 40px;
    font-size: 16px;
    line-height: 1.6;
  }
  .contact__row { display: flex; align-items: center; gap: 10px; }
  .contact__icon {
    width: 20px; height: 20px;
    background: var(--ink);
    border-radius: 3px;
    display: inline-flex;
    align-items: center;
    justify-content: center;
  }
  .card--front .contact { font-size: 14px; bottom: 36px; }
  .identity {
    position: absolute;
    right: 36px; top: 124px;
    text-align: right;
  }
  .identity__name { font-size: 24px; letter-spacing: -0.3px; }
  .identity__title { font-size: 13px; color: var(--muted); margin-top: 4px; }
</style>
</head>
<body>

  <section class="card card--front">
    <svg class="card__band" viewBox="0 0 120 309" aria-hidden="true">
      <polygon points="0,0 112,0 62,309 0,309" fill="var(--band)"/>
    </svg>
    <div class="brand">
      <span class="brand__dot" aria-hidden="true"></span>
      <p class="brand__name">Bright Meadow Fund</p>
    </div>
    <div class="identity">
      <p class="identity__name">Morgan Falkner</p>
      <p class="identity__title">Founder</p>
    </div>
    <div class="contact">
      <p>2316 Whitcombe Ave Harlow Springs, NV 93147</p>
      <p class="contact__row">
        <span class="contact__icon"><svg width="12" height="12" viewBox="0 0 24 24"><path fill="#fff" d="M6.6 10.8a15 15 0 0 0 6.6 6.6l2.2-2.2a1 1 0 0 1 1-.25 11.4 11.4 0 0 0 3.6.57 1 1 0 0 1 1 1V20a1 1 0 0 1-1 1A17 17 0 0 1 3 4a1 1 0 0 1 1-1h3.5a1 1 0 0 1 1 1c0 1.25.2 2.45.57 3.57a1 1 0 0 1-.25 1z"/></svg></span>
        541-317-6089
      </p>
      <p class="contact__row">
        <span class="contact__icon"><svg width="12" height="12" viewBox="0 0 24 24"><path fill="none" stroke="#fff" stroke-width="2" d="M3 6h18v12H3z M3 6l9 7 9-7"/></svg></span>
        morgan.falkner@brightmeadowfund.org
      </p>
    </div>
  </section>

  <section class="card card--back">
    <svg class="card__band" viewBox="0 0 120 309" aria-hidden="true">
      <polygon points="0,0 112,0 62,309 0,309" fill="var(--band)"/>
    </svg>
    <div class="brand">
      <span class="brand__dot" aria-hidden="true"></span>
      <p class="brand__name">Bright Meadow Fund</p>
    </div>
    <div class="contact">
      <p>2316 Whitcombe Ave Harlow Springs, NV 93147</p>
      <p class="contact__row">
        <span class="contact__icon"><svg width="12" height="12" viewBox="0 0 24 24"><path fill="#fff" d="M6.6 10.8a15 15 0 0 0 6.6 6.6l2.2-2.2a1 1 0 0 1 1-.25 11.4 11.4 0 0 0 3.6.57 1 1 0 0 1 1 1V20a1 1 0 0 1-1 1A17 17 0 0 1 3 4a1 1 0 0 1 1-1h3.5a1 1 0 0 1 1 1c0 1.25.2 2.45.57 3.57a1 1 0 0 1-.25 1z"/></svg></span>
        541-317-6089
      </p>
      <p class="contact__row">
        <span class="contact__icon"><svg width="12" height="12" viewBox="0 0 24 24"><path fill="none" stroke="#fff" stroke-width="2" d="M3 6h18v12H3z M3 6l9 7 9-7"/></svg></span>
        morgan.falkner@brightmeadowfund.org
      </p>
    </div>
  </section>

</body>
</html>
```